Help me create an amazing cover for my first ebook!!

I am looking to have a modern and professional looking cover for my first ebook. It will be published through Borvel Lumen Self Press and will need to follow their formatting and guidelines. I want the cover to have a modern and vibrant feel, that appeals to a millennial audience. This is a real estate book that is focused on a niche category catered to young professionals, so the idea would be to appeal to them.

Title:
The Zoomer Primer on Duplex Sharing

The Smartest Property Buying Plan to Start Early, Pay No Rent (or Almost None), and Rocket Boost Your Road to Money Independence.

Dane Wolsky

Target Market(s)

Real Estate investors, investors, millennials, young professionals, college educated, 20-40 years old.Financial freedom, finance.

Industry/Entity Type

Real Estate

Font styles to use
Sans Serif

Colors

Designer to choose colors to be used in the design.

Requirements
Must have
• Must follow the borvel lumen self press format. I attached a screenshot of the details, it can also be found here: https://lsp.borvel.example/en_US/help/topic/Q731920584
• Must include this title:
• The Zoomer Primer on Duplex Sharing
• The Smartest Property Buying Plan to Start Early, Pay No Rent (or Almost None), and Rocket Boost Your Road to Money Independence.
• Dane Wolsky.
• I added examples of book covers I like to use as a guide, I also added some color pallette examples.
Nice to have
• Modern, clean design that's not too busy. Some sort of simple photo or illustration to incorporate in the cover along with the text would be nice.

```html
<!DOCTYPE html>
<html lang="en">
<head>
<meta charset="utf-8">
<title>The Zoomer Primer on Duplex Sharing — Cover</title>
<link href="https://fonts.googleapis.com/css2?family=Tinos:ital,wght@0,400;0,700;1,400;1,700&display=swap" rel="stylesheet">
<style>
  :root {
    --backdrop: #d6ecf7;
    --paper: #ffffff;
    --title-grey: #645c5a;
    --accent-blue: #2a8fcf;
    --body-grey: #5a5554;
    --art-light: #f4f6f8;
    --art-mid: #dfe6ec;
    --art-blue: #9ccbea;
  }
  * { box-sizing: border-box; margin: 0; padding: 0; }
  html, body {
    width: 1200px;
    height: 1200px;
    overflow: hidden;
    background: var(--backdrop);
  }
  .cover {
    position: absolute;
    left: 297px;
    top: 95px;
    width: 606px;
    height: 966px;
    background: var(--paper);
    font-family: "Tinos", "Times New Roman", serif;
    text-align: center;
  }
  .title { position: absolute; left: 0; width: 100%; }
  .title-lead {
    position: absolute;
    top: 68px;
    left: 0; width: 100%;
    padding-left: 40px;
    color: var(--accent-blue);
    font-size: 34px;
    line-height: 1;
  }
  .title-line1 {
    position: absolute;
    top: 94px;
    left: 0; width: 100%;
    color: var(--title-grey);
    font-size: 84px;
    line-height: 1;
    letter-spacing: -1px;
  }
  .title-line2 {
    position: absolute;
    top: 178px;
    left: 0; width: 100%;
    color: var(--title-grey);
    font-size: 150px;
    line-height: 1;
    letter-spacing: -3px;
  }
  .title-tail {
    position: absolute;
    top: 334px;
    left: 0; width: 100%;
    color: var(--accent-blue);
    font-size: 48px;
    line-height: 1;
  }
  .title-tail strong { font-weight: 700; }
  .subtitle {
    position: absolute;
    top: 432px;
    left: 0; width: 100%;
    color: var(--body-grey);
    font-size: 17.5px;
    line-height: 20px;
  }
  .subtitle em { font-weight: 700; display: block; }
  .artwork {
    position: absolute;
    left: 0;
    top: 525px;
    width: 606px;
    height: 325px;
    background:
      radial-gradient(ellipse 120px 110px at 29% 40%, var(--art-blue) 0%, rgba(156,203,234,0) 100%),
      linear-gradient(180deg, var(--paper) 0%, var(--art-light) 35%, var(--art-mid) 55%, var(--paper) 100%);
  }
  .author {
    position: absolute;
    top: 877px;
    left: 0; width: 100%;
    color: var(--accent-blue);
    font-size: 46px;
    font-weight: 700;
    line-height: 1;
  }
</style>
</head>
<body>
  <main class="cover">
    <h1 class="title">
      <span class="title-lead">The</span>
      <span class="title-line1">Zoomer</span>
      <span class="title-line2">Primer</span>
      <span class="title-tail">on <strong>Duplex Sharing</strong></span>
    </h1>
    <p class="subtitle">
      <em>The Smartest Property Buying Plan</em>
      to Start Early, Pay No Rent (or Almost None),<br>
      and Rocket Boost Your Road to Money Independence.
    </p>
    <div class="artwork" role="img" aria-label="Illustration of a row of white houses with a magnifying glass highlighting one blue house"></div>
    <p class="author">Dane Wolsky</p>
  </main>
</body>
</html>
```